super clean and modern easy to read. Scandinavian type design.

Hi everyone, we need a wall menu for our retail space. We'd like something that goes along with the style of our website and is also editable (in case we change prices later on). The dimensions for the menu will be about 72 inches wide and about 48 inches high and it will be attached to the wall in our business. Please pull menu wording from this link: http://www.velsaskinloft.com/services

Feel free to shorten the descriptions.

The main sections of the menu are:
mod facials
enhancements
add-ons ($15, $20, and $30)
celebrity facials

Please include the picture of the woman on our homepage in the menu. I'll attach an image.

We would like to start with our process to simplify the steps we take.
1.)Complimentary skin analysis
2.) Choose your service
3.) Choose your products (recommendations are given)
4.) Enjoy!
5.) Further your results with take home products

Last little note, we can email you a larger Logo...Pixel Forum would not let us upload the largest file that we have for the logo.

Target Market(s)

young, fun, hip, suburban women and men.

Industry/Entity Type

Retail

Font styles to use
Sans Serif

Requirements
Must have
• Not too much orange. Keep it clean and not too busy.
• the menu should make it super easy for someone to walk into the store and figure out the process.
• the 5 steps should be listed out first
• the 2 basic facials
• the add ons
• the enhancements (by price)
• the celebrity facials
• Advanced peels
• colors should be mainly blue and white (website) some orange used for framing categories or black. I like clean and not too busy. no cheesy.
Nice to have
• see colors on website. see style.
Should not have
• no clip art! no cursive formal writing.

```html
<!DOCTYPE html>
<html lang="en">
<head>
<meta charset="utf-8">
<title>Velsa Skin Loft – Service Menu</title>
<link href="https://fonts.googleapis.com/css2?family=Roboto:ital,wght@0,400;0,500;0,700;0,900;1,900&family=Roboto+Condensed:wght@500;700&display=swap" rel="stylesheet">
<style>
  :root{
    --teal:#5bc4d1;
    --teal-soft:#dff3f6;
    --orange:#ef8a23;
    --grey:#a9aaac;
    --ink:#1b1b1b;
    --body:#2b2b2b;
    --white:#ffffff;
  }
  *{margin:0;padding:0;box-sizing:border-box}
  html,body{width:1200px;height:814px;overflow:hidden;background:var(--white)}
  body{font-family:"Roboto",Arial,sans-serif;color:var(--body)}
  .menu{position:relative;width:1200px;height:814px;
    background:linear-gradient(90deg,#f3fbfc 0%,#ffffff 30%,#ffffff 62%,#eaf7f9 85%,#c9ecf1 100%);overflow:hidden}

  /* process band */
  .steps{position:absolute;left:0;top:0;width:1200px;height:126px;background:var(--teal);
    display:flex;align-items:center;padding-left:20px}
  .step{display:flex;align-items:center;margin-right:14px}
  .step-num{width:58px;height:58px;border-radius:50%;background:var(--orange);color:var(--white);
    font:700 40px/58px "Roboto Condensed",sans-serif;text-align:center;flex:none;margin-right:8px}
  .step-text{color:var(--white);font:500 28px/31px "Roboto Condensed",sans-serif;letter-spacing:-.3px}
  .step-text small{font-size:13px;line-height:12px;display:inline-block;vertical-align:bottom}

  /* section headings */
  .sec-title{position:absolute;font:700 37px/1 "Roboto",sans-serif;color:var(--teal);letter-spacing:-.5px;
    white-space:nowrap;padding-bottom:6px;border-bottom:2px dashed var(--orange)}
  .dots{display:inline-block;vertical-align:middle;margin-left:6px}
  .dots i{display:inline-block;width:22px;height:22px;border-radius:50%;background:var(--orange);margin-left:1px}

  .col{position:absolute;font-size:12.4px;line-height:13.6px}
  .item-title{font-weight:700;font-size:15.5px;color:var(--ink);margin-bottom:3px}
  .col ul{list-style:none}
  .col li{position:relative;padding-left:8px}
  .col li::before{content:"•";position:absolute;left:0}
  .series{font-weight:700;font-size:13.5px;color:var(--ink);margin:4px 0 0 8px}

  .list{position:absolute;list-style:none;font-size:14px;line-height:16px}
  .list li{position:relative;padding-left:10px;margin-bottom:4px}
  .list li::before{content:"•";position:absolute;left:0;font-weight:700}
  .list b{color:var(--ink);font-weight:700}

  .arrow{position:absolute;width:96px;height:72px}

  .brand-rule{position:absolute;left:362px;width:404px;height:2px;background:var(--teal)}
  .brand-name{position:absolute;left:362px;top:408px;width:404px;text-align:center;
    font:700 64px/1 "Roboto",sans-serif;color:var(--teal);letter-spacing:-2px}
  .social{position:absolute;left:496px;top:521px;display:flex;gap:7px}
  .social span{width:23px;height:23px;border-radius:50%;border:2px solid var(--teal);background:var(--white)}

  /* signature box */
  .results{position:absolute;left:52px;top:557px;width:718px;height:201px;border:2.5px solid var(--orange);background:var(--white)}
  .results-tab{position:absolute;left:3px;top:3px;width:290px;height:46px;
    background:linear-gradient(90deg,var(--teal) 0%,#9fdbe3 70%,rgba(255,255,255,0) 100%);
    font:italic 900 27px/46px "Roboto",sans-serif;color:var(--ink);padding-left:12px;letter-spacing:-.6px}
  .celeb-title{position:absolute;left:305px;top:6px;font:700 33px/1 "Roboto",sans-serif;color:var(--teal);
    letter-spacing:-.5px;padding-bottom:4px;border-bottom:2px dashed var(--orange);white-space:nowrap}
  .celeb-title svg{vertical-align:middle;margin-left:3px}
  .facial{position:absolute;top:62px;font-size:9.6px;line-height:12px}
  .facial h4{font-size:14px;line-height:14.5px;font-weight:700;color:var(--ink)}
  .facial .who{font-size:14px;line-height:14.5px;color:var(--ink);display:block;margin-bottom:1px}
  .divider{position:absolute;top:60px;width:1.5px;height:118px;background:var(--orange)}
</style>
</head>
<body>
<main class="menu">

  <header class="steps">
    <div class="step"><div class="step-num">1.</div><div class="step-text">choose your<br>facial</div></div>
    <div class="step"><div class="step-num">2.</div><div class="step-text">complimentary<br>skin analysis</div></div>
    <div class="step"><div class="step-num">3.</div><div class="step-text">choose<br>enhancement<br>products <small>(advice<br>given)</small></div></div>
    <div class="step"><div class="step-num">4.</div><div class="step-text">relax +<br>enjoy!</div></div>
    <div class="step"><div class="step-num">5.</div><div class="step-text">extend results with<br>take home products</div></div>
  </header>

  <!-- facials -->
  <h2 class="sec-title" style="left:48px;top:158px">velsa facials<span class="dots"><i></i><i></i></span></h2>
  <section class="col" style="left:48px;top:210px;width:300px">
    <div class="item-title">velsa essential 30 min | $49</div>
    <ul>
      <li>deep breathing with lavender essential oils</li>
      <li>includes In-depth skin analysis, with recommendations</li>
      <li>power cleanse x2, hot steam, exfoliation high frequency treatment or facial vacuum</li>
      <li>Shiatsu style massage</li>
      <li>lavender hot towel treatment</li>
      <li>customized mask, sun protection and lip treatment</li>
    </ul>
    <div class="series">Series of 3 $125</div>
    <div class="item-title" style="margin-top:12px">velsa essential 45 min | $69</div>
    <ul>
      <li>facial customized specifically for your skins needs</li>
      <li>deep cleansing, exfoliation and hydration</li>
      <li>may include a bubbling pore mask, a pore vacuum, high frequency, special hydration mask</li>
      <li>lymphatic draining facial and neck massage</li>
      <li>hand, arm and décolleté massage</li>
    </ul>
    <div class="series">Series of 3 $165</div>
  </section>

  <!-- arrows -->
  <svg class="arrow" style="left:320px;top:242px" viewBox="0 0 96 72" aria-hidden="true">
    <g fill="var(--orange)"><rect x="0" y="22" width="10" height="30"/><rect x="15" y="22" width="10" height="30"/><rect x="30" y="22" width="10" height="30"/><path d="M46 22h16V0l34 36-34 36V52H46z"/></g>
  </svg>
  <svg class="arrow" style="left:662px;top:242px" viewBox="0 0 96 72" aria-hidden="true">
    <g fill="var(--orange)"><rect x="0" y="22" width="10" height="30"/><rect x="15" y="22" width="10" height="30"/><rect x="30" y="22" width="10" height="30"/><path d="M46 22h16V0l34 36-34 36V52H46z"/></g>
  </svg>

  <!-- enhancements -->
  <h2 class="sec-title" style="left:390px;top:158px">enhancements $10<span class="dots"><i></i><i></i></span></h2>
  <ul class="list" style="left:428px;top:214px;width:260px">
    <li><b>vitamin c</b> (radiance + fine lines)</li>
    <li><b>peptide (</b>plump &amp; smooth)</li>
    <li><b>hyaluronic acid</b><br>(moisture.anti-aging)</li>
    <li><b>retinol</b> (fine lines.age spots)</li>
    <li><b>dehydrated eye treatment</b></li>
    <li><b>cherry enzyme peel</b><br>(antioxidant, healthy glow)</li>
    <li><b>pumpkin</b> (revitalizes, reduce lines)</li>
  </ul>

  <!-- brand -->
  <div class="brand-rule" style="top:398px"></div>
  <div class="brand-name">velsa skinloft</div>
  <div class="brand-rule" style="top:532px"></div>
  <div class="social" aria-hidden="true"><span></span><span></span><span></span><span></span></div>

  <!-- add-ons -->
  <h2 class="sec-title" style="left:802px;top:158px">add-ons $15<span class="dots"><i></i><i></i></span></h2>
  <ul class="list" style="left:802px;top:210px;width:360px">
    <li><b>wax - brow, chin or lip</b> (touch up)</li>
    <li><b>magnetic mud mask</b><br>(nourish.mineral infusion)</li>
    <li><b>peppermint/eucalyptus scalp massage</b><br>(invigorating.stress reduction)</li>
    <li><b>beard Oil Treatment</b><br>(softens and protects)</li>
  </ul>

  <h2 class="sec-title" style="left:802px;top:345px">add-ons $20<span class="dots"><i></i><i></i></span></h2>
  <ul class="list" style="left:802px;top:393px;width:360px">
    <li><b>me time - 20 min extra massage</b>(relax.enjoy)</li>
    <li><b>hand rejuvenation peel or microderm</b><br>(exfoliating, antiaging)</li>
  </ul>

  <h2 class="sec-title" style="left:802px;top:463px">add-ons $30<span class="dots"><i></i><i></i></span></h2>
  <ul class="list" style="left:802px;top:512px;width:360px;font-size:13.4px;line-height:15px">
    <li><b>crystal microdermabrasion for face and neck or declotte - 2 passes</b> (fine lines, smoothing)</li>
    <li><b>diamond microdermabrasion for face and neck or declotte - 2 passes</b> (fine lines, smoothing)</li>
    <li><b>led light therapy - 20 min</b> (red antiaging) (blue acne)</li>
    <li><b>decollete treatment</b><br>(peel or microderm) (anti-aging, fine lines)</li>
    <li><b>whole face wax</b> (except brows)</li>
    <li><b>hand treatment - peel + microderm</b><br>(double exfoliation for antiaging)</li>
    <li><b>facial hydration cocktail -1 pass of microderm + 7 advanced serums to fully hydrate your skin</b> (glow,renew)</li>
    <li><b>microcurrent eye, mouth, or chin</b> (non-surgical face lift)</li>
  </ul>

  <!-- celebrity facials -->
  <section class="results">
    <div class="results-tab">for maximum results...</div>
    <h2 class="celeb-title">celebrity facials<svg width="50" height="24" viewBox="0 0 50 24" aria-hidden="true"><g fill="var(--orange)"><path d="M12 1l3.4 7.2 7.8.9-5.8 5.3 1.6 7.7L12 18.2 5 22.1l1.6-7.7L.8 9.1l7.8-.9z"/><path d="M37 1l3.4 7.2 7.8.9-5.8 5.3 1.6 7.7L37 18.2 30 22.1l1.6-7.7-5.8-5.3 7.8-.9z"/></g></svg></h2>

    <div class="facial" style="left:26px;width:130px">
      <h4>oxygen facial<br>50 min | $130</h4>
      <span class="who">(marisol vey's secret to red carpet skin)</span>
      Rehydrates and plumps skin in less than an hour. naturally binds moisture within the skin for an instant glow.
    </div>
    <div class="divider" style="left:163px"></div>
    <div class="facial" style="left:170px;width:140px">
      <h4>led therapy facial<br>50 min | $130</h4>
      <span class="who">(Tessa Corin's fav)</span>
      We use LED for anti-aging, correcting discoloration, healing acne, and reversing the effects of sun damage. LED has been FDA approved for beauty treatments.
    </div>
    <div class="divider" style="left:318px"></div>
    <div class="facial" style="left:325px;width:150px">
      <h4>Lumina Non Surgical Facelift| 50 min | $130</h4>
      <span class="who">(Janelle Ortiz)</span>
      non-surgical facelift<br>first time client $99<br>only sold in series (depends on age and condition of skin)<br>series of 3 $ series of 6 $<br>series of 10 $
    </div>
    <div class="divider" style="left:487px"></div>
    <div class="facial" style="left:506px;width:200px">
      <h4>50 min | micro + peel | $130</h4>
      decrease fine lines &amp; wrinkles, reverses sun damage reduces scarring, rough texture, discoloration
      <h4 style="margin-top:11px">50 min Advanced Peel | $130</h4>
      Advanced peels reverse sun damage, wrinkles, acne, signs of aging
    </div>
  </section>

</main>
</body>
</html>
```